Corvellan Solutions needs an IT Managed Services Website and the logo needs to be updated

We need a new website for our 25 year old IT Managed Services Company. Our company specializes in listening to and understanding our customer needs and goals. Our customers include SME's and Corporates in industries ranging from Medical, Legal, Industrial & Manufacturing and Financial. The services that we offer include: Managed IT Services, Remote Monitoring and Management and Virtualisation. Corvellan Solutions takes technology and makes the lives of our customers easier by applying it appropriately. In the same way, we want a website that is as pleasing to the eye, as it is simple to find information and call to action. The website should say as much in design as it does in content and it should be saying that Corvellan Solutions is your technology partner that listens to you, understands you, delivers solutions and is loyal in our relationship with you. Aesthetically, we want to go for something a little warmer than blue and white, but want to err on the side of professional.
The Logo: We need the "computer" and "ltd" to be removed from the logo. We want to keep the @ on the "u". We would like to freshen up the logo inline with the website design in terms of look and feel and colour.

Target Market(s)

Businesses that require IT Managed Services

Logo Text

Corvellan Solutions

Coding

Coded - Design and coding required

Number of Pages Required

5+ page

Font styles to use
Sans Serif

Colors

Designer to choose colors to be used in the design.

Requirements
Must have
• Each page must have a call to action.

```html
<!DOCTYPE html>
<html lang="en">
<head>
<meta charset="utf-8">
<title>Corvellan Solutions – Your Computing Solution Partner</title>
<link href="https://fonts.googleapis.com/css2?family=Roboto:wght@300;400;500;700;900&display=swap" rel="stylesheet">
<style>
:root{
  --navy:#0c1642;
  --navy-deep:#08102f;
  --royal:#1f47c9;
  --bright:#1c5fe0;
  --sky:#6fc7ea;
  --violet:#3a43a8;
  --ink:#1d1f2b;
  --muted:#6c7080;
  --white:#ffffff;
  --footer-ink:#2a3a5a;
}
*{margin:0;padding:0;box-sizing:border-box}
html,body{width:1200px;height:3982px;overflow:hidden}
body{position:relative;font-family:"Roboto",Arial,sans-serif;color:var(--ink);background:var(--white)}
.abs{position:absolute}
.backdrop{position:absolute;left:0;top:0}

/* header + hero */
.hero{left:0;top:0;width:1200px;height:685px;background:linear-gradient(120deg,#1a2a86 0%,#2846b8 45%,#4f7fdc 70%,#1c2f8f 100%)}
.hero-shade{left:0;top:0;width:1200px;height:685px;background:linear-gradient(180deg,rgba(8,16,47,.55) 0%,rgba(8,16,47,0) 30%,rgba(8,16,47,0) 75%,rgba(8,16,47,.6) 100%)}
.topbar{left:690px;top:18px;display:flex;align-items:center;gap:8px;color:var(--white);font-size:13px;font-weight:500}
.dot{width:15px;height:15px;border-radius:50%;background:var(--white)}
.logo{left:135px;top:36px;display:flex;align-items:center;gap:8px;color:var(--white);font-weight:900;font-size:30px;line-height:1}
.logo-mark{width:36px;height:36px;border:4px solid var(--white);border-radius:50%}
.nav{left:532px;top:64px;display:flex;gap:30px;color:var(--white);font-size:14px;font-weight:700;letter-spacing:.3px}
.headline{left:137px;top:178px;color:var(--white);font-weight:900;font-size:60px;line-height:1.05;letter-spacing:-.5px}
.cta-hero{left:330px;top:362px;width:212px;height:58px;background:var(--bright);border-radius:4px;color:var(--white);text-align:center;padding-top:9px}
.cta-hero small{display:block;font-size:13px;font-weight:700}
.cta-hero strong{display:block;font-size:19px;font-weight:900;letter-spacing:.5px}
.remote{left:282px;top:620px;display:flex;align-items:center;gap:18px;color:var(--white)}
.remote h3{font-size:23px;font-weight:900}
.pills{display:flex;border:2px solid var(--white);border-radius:20px;overflow:hidden}
.pills span{padding:6px 22px;font-size:14px;font-weight:700}
.pills .on{background:var(--white);color:var(--bright)}

/* shared */
.photo{border-radius:2px}
.h-blue{color:var(--bright)}
.btn{display:inline-block;background:var(--bright);color:var(--white);font-size:12px;font-weight:700;padding:12px 24px;border-radius:3px;letter-spacing:.3px}
.btn-navy{background:#1a4fb5}
.body-text{font-size:13px;line-height:1.6;color:var(--muted)}

/* about */
.about{left:137px;top:750px;width:380px}
.about h2{font-size:40px;font-weight:900;line-height:1.15}
.about .lead{margin-top:22px;font-size:13px;font-weight:700;line-height:1.6;color:var(--ink)}
.about .body-text{margin-top:18px}

/* help */
.help{left:620px;top:1195px;width:450px;color:var(--white)}
.help h2{font-size:42px;font-weight:900;line-height:1.12}
.help h2 .h-blue{color:#2f6bf2}
.help h4{margin-top:16px;font-size:19px;font-weight:500}
.help p{margin-top:8px;font-size:12.5px;line-height:1.65;color:#e4e8f5}
.help .btn{margin-top:20px}

.monitor{left:137px;top:1725px;width:380px}
.monitor h4{font-size:18px;font-weight:500;color:#2b3450}
.monitor p{margin-top:10px;font-size:12.5px;line-height:1.65;color:#3c4a66}
.monitor .btn{margin-top:26px}

.virtual{left:628px;top:2248px;width:440px}
.virtual h4{font-size:18px;font-weight:500;color:var(--ink)}
.virtual p{margin-top:8px}
.virtual .btn{margin-top:22px}

/* why */
.why{left:137px;top:2700px;width:460px;color:var(--white)}
.why h2{font-size:42px;font-weight:900;line-height:1.12}
.why .lead{margin-top:16px;font-size:13px;font-weight:700;line-height:1.6}
.why p{margin-top:16px;font-size:12.5px;line-height:1.65;color:#e2e6f7}
.why .btn{margin-top:22px}
.circle-photo{border-radius:50%;border:6px solid var(--white)}

/* services */
.services-title{left:168px;top:3255px;font-size:42px;font-weight:900}
.service{width:300px;text-align:center}
.service-ring{width:118px;height:118px;margin:0 auto;display:block}
.service h5{margin-top:22px;font-size:15px;font-weight:700;line-height:1.3}
.service p{margin-top:6px;font-size:13px;line-height:1.4;color:#2a2d3a}

/* footer */
.footer{left:0;top:3717px;width:1200px;height:213px;background:var(--sky)}
.footer-col{top:3748px;color:var(--footer-ink)}
.footer-col h6{font-size:14px;font-weight:700}
.footer-col p{margin-top:8px;font-size:12.5px;line-height:1.55;color:#3f5a82}
.bottombar{left:0;top:3930px;width:1200px;height:52px;background:var(--navy-deep)}
.copy{left:137px;top:3948px;color:var(--white);font-size:12px}
.socials{left:565px;top:3949px;display:flex;gap:6px}
.up{left:876px;top:3902px;width:56px;height:40px;background:var(--navy-deep)}
</style>
</head>
<body>

<svg class="backdrop" width="1200" height="3982" viewBox="0 0 1200 3982" aria-hidden="true">
  <defs>
    <linearGradient id="navyGrad" x1="0" y1="0" x2="1" y2="1">
      <stop offset="0" stop-color="#0a1440"/>
      <stop offset="1" stop-color="#142a6e"/>
    </linearGradient>
    <linearGradient id="whyGrad" x1="0" y1="0" x2="1" y2="1">
      <stop offset="0" stop-color="#2d3a9a"/>
      <stop offset=".55" stop-color="#3f4fb4"/>
      <stop offset="1" stop-color="#7b86d6"/>
    </linearGradient>
  </defs>
  <polygon points="0,1572 1200,1592 1200,2205 0,2125" fill="#6fc7ea"/>
  <polygon points="0,1085 1200,1180 1200,1592 0,1700" fill="url(#navyGrad)"/>
  <polygon points="0,2590 1200,2520 1200,3218 0,3195" fill="url(#whyGrad)"/>
</svg>

<!-- hero -->
<div class="abs hero" role="img" aria-label="Hands holding a tablet with glowing location pins in a blue-toned office"></div>
<div class="abs hero-shade"></div>

<div class="abs topbar">
  <span class="dot"></span><span class="dot"></span><span class="dot"></span><span class="dot"></span>
  <span>&#9993; info@corvellansolutions.com</span>
  <span>&#9742; 555.010.2468</span>
</div>
<div class="abs logo"><span class="logo-mark"></span><span>Corvellan Solutions</span></div>
<nav class="abs nav"><span>HOME</span><span>SERVICES</span><span>ABOUT US</span><span>TESTIMONIALS</span><span>BLOG</span><span>CONTACT</span><span>&#9906;</span></nav>

<h1 class="abs headline">YOUR COMPUTING<br>SOLUTION PARTNER</h1>
<div class="abs cta-hero"><small>Get a FREE Consultation</small><strong>SCHEDULE NOW</strong></div>

<div class="abs remote">
  <h3>GET OUR REMOTE ASSISTANCE</h3>
  <div class="pills"><span>FOR PC</span><span class="on">FOR MOBILE</span></div>
</div>

<!-- about -->
<section class="abs about">
  <h2><span class="h-blue">About</span><br>Corvellan Solutions</h2>
  <p class="lead">Corvellan Solutions is an IT Managed Services Provider (MSP) that has more than 25 years experience growing and collaborating in the IT industry.</p>
  <p class="body-text">Our expertise lies in listening to and understanding our more than 1500 customers' needs and delivering the best value for money IT infrastructure and technology solutions.</p>
  <p class="body-text" style="margin-top:4px">We believe in loyal and lasting relationships, creating a region within which your company can grow and outperform its own expectations.</p>
</section>
<div class="abs photo" style="left:546px;top:735px;width:509px;height:340px;background:linear-gradient(135deg,#5a4a3c,#8a7a68 50%,#3d3530)" role="img" aria-label="Team working together on laptops around a table"></div>

<!-- how can we help -->
<div class="abs photo" style="left:137px;top:1216px;width:377px;height:303px;background:linear-gradient(135deg,#2a3e5e,#7d8ea8 50%,#1e2a40)" role="img" aria-label="Network cables plugged into a server rack"></div>
<section class="abs help">
  <h2>How Can<br>Corvellan Solutions<br><span class="h-blue">help you?</span></h2>
  <h4>Managed IT Services</h4>
  <p>Corvellan brings a personal touch to you through our IT consulting services. We collaborate with partners across the globe to bring the best technology to you. You can rely on our expertise to design and maintain the most effective infrastructure for your business. Our quick and efficient support team will troubleshoot your IT problems and ensure your business continues to operate with minimum disruption.</p>
  <span class="btn">CALL US NOW</span>
</section>

<!-- remote monitoring -->
<section class="abs monitor">
  <h4>Remote Monitoring &amp; Management</h4>
  <p>Corvellan brings a personal touch to you through our IT consulting services. We collaborate with partners across the globe to bring the best technology to you. You can rely on our expertise to design and maintain the most effective infrastructure for your business. Our quick and efficient support team will troubleshoot your IT problems and ensure your business continues to operate with minimum disruption.</p>
  <span class="btn btn-navy">CALL US NOW</span>
</section>
<div class="abs photo" style="left:546px;top:1707px;width:509px;height:298px;background:linear-gradient(135deg,#1e2430,#56606e 50%,#2a303a)" role="img" aria-label="Monitoring room with many screens showing system dashboards"></div>

<!-- virtualisation -->
<div class="abs photo" style="left:137px;top:2204px;width:435px;height:292px;background:linear-gradient(135deg,#c9ced6,#8a929e 55%,#4e5560)" role="img" aria-label="Hand working on cables in an electrical and network cabinet"></div>
<section class="abs virtual">
  <h4>Virtualisation</h4>
  <p class="body-text">Corvellan brings you the high performance Hybrid Cloud, which reduces your total IT spend in comparison to competitors like Nimbus, Stratus and Cirrus. You will find that these virtual machines are easy to configure and migration is simple. With enterprise grade security and compliance you will have peace of mind about your data.</p>
  <span class="btn">CALL US NOW</span>
</section>

<!-- why choose -->
<section class="abs why">
  <h2>Why Choose<br>Corvellan Solutions</h2>
  <p class="lead">Corvellan Solutions was founded in 2003 and is in the business of collaborating with partners to bring the best technologies to you.</p>
  <p>We have more than 25 years experience in the IT industry, servicing customers across the region. Our customers come from different industry sectors including Medical, Financial, Real Estate, Legal and more. We work together with our customers as members of their teams to realise their IT visions and goals.</p>
  <p>We have collaborated with partners across the globe to ensure that we bring the most innovative and functional technology to our customers. We can provide you the best solution for your business.</p>
  <span class="btn">READ MORE</span>
</section>
<div class="abs circle-photo" style="left:615px;top:2637px;width:274px;height:274px;background:linear-gradient(135deg,#d8dde6,#8c96a8)" role="img" aria-label="Hands typing on a laptop beside paperwork"></div>
<div class="abs circle-photo" style="left:751px;top:2788px;width:238px;height:238px;background:linear-gradient(135deg,#4a5260,#a8b0bc)" role="img" aria-label="Person working at a computer in an office"></div>
<div class="abs circle-photo" style="left:669px;top:2955px;width:222px;height:222px;background:linear-gradient(135deg,#2c3440,#7c8898)" role="img" aria-label="Person wearing a virtual reality headset"></div>

<!-- services -->
<h2 class="abs services-title">Our <span class="h-blue">Services</span></h2>

<div class="abs service" style="left:82px;top:3354px">
  <svg class="service-ring" viewBox="0 0 118 118" aria-hidden="true">
    <circle cx="59" cy="59" r="54" fill="none" stroke="#1c5fe0" stroke-width="7" stroke-dasharray="260 80" transform="rotate(120 59 59)"/>
    <circle cx="59" cy="52" r="14" fill="none" stroke="#1d1f2b" stroke-width="3"/>
    <circle cx="59" cy="52" r="5" fill="#1d1f2b"/>
    <path d="M32 72 q10 14 27 14 q17 0 27 -14" fill="none" stroke="#1d1f2b" stroke-width="3"/>
  </svg>
  <h5>Managed IT Services</h5>
  <p>Lorem ipsum dolor sit amet, consectetur adipiscing elit. Ut viverra arcu non pulvinar gravida. Nulla vel eros nibh. Nunc id porta augue, euismod accumsan tortor.</p>
</div>
<div class="abs service" style="left:435px;top:3354px">
  <svg class="service-ring" viewBox="0 0 118 118" aria-hidden="true">
    <circle cx="59" cy="59" r="54" fill="none" stroke="#1c5fe0" stroke-width="7" stroke-dasharray="260 80" transform="rotate(120 59 59)"/>
    <rect x="32" y="36" width="54" height="42" rx="4" fill="none" stroke="#1d1f2b" stroke-width="3"/>
    <circle cx="66" cy="48" r="4" fill="#1d1f2b"/><circle cx="52" cy="57" r="4" fill="#1d1f2b"/><circle cx="66" cy="66" r="4" fill="#1d1f2b"/>
    <path d="M66 48 L52 57 L66 66" fill="none" stroke="#1d1f2b" stroke-width="2"/>
    <path d="M50 86 h18" stroke="#1d1f2b" stroke-width="3"/>
  </svg>
  <h5>Remote Monitoring and<br>Management</h5>
  <p>Lorem ipsum dolor sit amet, consectetur adipiscing elit. Ut viverra arcu non pulvinar gravida. Nulla vel eros nibh. Nunc id porta augue, euismod accumsan tortor.</p>
</div>
<div class="abs service" style="left:786px;top:3354px">
  <svg class="service-ring" viewBox="0 0 118 118" aria-hidden="true">
    <circle cx="59" cy="59" r="54" fill="none" stroke="#1c5fe0" stroke-width="7" stroke-dasharray="260 80" transform="rotate(120 59 59)"/>
    <circle cx="59" cy="56" r="24" fill="none" stroke="#1d1f2b" stroke-width="3"/>
    <rect x="34" y="50" width="50" height="16" rx="6" fill="none" stroke="#1d1f2b" stroke-width="3"/>
    <path d="M42 80 h34" stroke="#1d1f2b" stroke-width="3"/>
  </svg>
  <h5>Virtualisation</h5>
  <p>Lorem ipsum dolor sit amet, consectetur adipiscing elit. Ut viverra arcu non pulvinar gravida. Nulla vel eros nibh. Nunc id porta augue, euismod accumsan tortor.</p>
</div>

<!-- footer -->
<footer>
  <div class="abs footer"></div>
  <div class="abs footer-col" style="left:137px;width:220px">
    <h6>About Corvellan Solutions</h6>
    <p>Corvellan Solutions is an IT Managed Services Provider (MSP) that has more than 25 years experience.</p>
    <p style="margin-top:18px">Read More</p>
  </div>
  <div class="abs footer-col" style="left:535px;width:160px">
    <h6>Services</h6>
    <p>Managed IT Services</p>
    <p style="margin-top:4px">Remote Monitoring and Management</p>
    <p style="margin-top:4px">Virtualisation</p>
  </div>
  <div class="abs footer-col" style="left:832px;width:240px">
    <h6>Contact</h6>
    <p>Corvellan Solutions<br>14 Harbour Lane, Suite 200<br>Eastport, EP 4821<br>Phone: 555.010.2468<br>Fax: 555.010.2469<br>Email: info@corvellansolutions.com</p>
  </div>
  <div class="abs bottombar"></div>
  <div class="abs up">
    <svg width="56" height="40" viewBox="0 0 56 40" aria-hidden="true"><path d="M20 24 L28 16 L36 24" fill="none" stroke="#ffffff" stroke-width="2.5"/></svg>
  </div>
  <p class="abs copy">© Copyright 2018 CorvellanSolutions</p>
  <div class="abs socials"><span class="dot"></span><span class="dot"></span><span class="dot"></span><span class="dot"></span></div>
</footer>

</body>
</html>
```